Design Packaging for Monte Alba Coffee

Please look at website at www.montealbacoffeecompany.example
Need packaging for new coffee company. The size is: 6 x 9 x 3"

```html
<!DOCTYPE html>
<html lang="en">
<head>
<meta charset="utf-8">
<title>Monte Alba Coffee – Roasted Coffee Pouch</title>
<link rel="stylesheet" href="https://fonts.googleapis.com/css2?family=Oswald:wght@500;700&display=swap">
<style>
  :root {
    --backdrop: #dcdbd7;
    --stripe-maroon: #4b2327;
    --stripe-dark: #2d2020;
    --label-cream: #ece6d8;
    --type-cream: #efe9dc;
    --type-gold: #c49256;
    --shade-brown: #7a5a48;
    --bean-dark: #3a1d10;
    --bean-mid: #6b3a20;
    --bean-light: #8e5432;
  }
  html, body {
    margin: 0;
    width: 1200px;
    height: 900px;
    overflow: hidden;
    background: var(--backdrop);
  }
  .pouch {
    position: absolute;
    left: 447px;
    top: 207px;
    width: 300px;
    height: 500px;
    background: repeating-linear-gradient(90deg,
      var(--stripe-maroon) 0 26px,
      var(--stripe-dark) 26px 52px);
    overflow: hidden;
    font-family: "Oswald", sans-serif;
  }
  .pouch-shapes {
    position: absolute;
    inset: 0;
  }
  .brand {
    position: absolute;
    left: 56px;
    top: 44px;
    display: flex;
    align-items: center;
    gap: 9px;
    color: var(--type-gold);
    font-weight: 500;
    font-size: 25px;
    letter-spacing: 0.5px;
    line-height: 1;
  }
  .brand-dot {
    width: 30px;
    height: 30px;
    border-radius: 50%;
    background: var(--type-gold);
  }
  .claim, .grade {
    position: absolute;
    left: 0;
    right: 0;
    text-align: center;
    color: var(--type-gold);
    font-weight: 500;
    line-height: 1;
  }
  .claim { top: 168px; font-size: 22px; letter-spacing: 0.5px; }
  .grade { top: 336px; font-size: 18px; letter-spacing: 0.6px; }
  .product-name {
    position: absolute;
    left: 0;
    right: 0;
    top: 188px;
    margin: 0;
    text-align: center;
    color: var(--type-cream);
    font-weight: 700;
    font-size: 62px;
    line-height: 66px;
    letter-spacing: 1px;
    text-shadow: 3px 3px 0 var(--shade-brown);
  }
  .bean-window {
    position: absolute;
    left: 0;
    bottom: 0;
    width: 300px;
    height: 90px;
  }
</style>
</head>
<body>
  <div class="pouch">
    <svg class="pouch-shapes" width="300" height="500" viewBox="0 0 300 500">
      <polygon class="top-label" points="36,0 264,0 264,88 150,140 36,88" fill="var(--label-cream)"/>
    </svg>

    <div class="brand"><span class="brand-dot"></span>MONTE ALBA</div>

    <div class="claim">100% ORGANIC</div>
    <h1 class="product-name">ROASTED<br>COFFEE</h1>
    <div class="grade">PREMIUM QUALITY</div>

    <svg class="bean-window" viewBox="0 0 300 90" role="img" aria-label="Photograph of roasted coffee beans">
      <defs>
        <linearGradient id="beans" x1="0" y1="0" x2="0" y2="1">
          <stop offset="0" stop-color="var(--bean-light)"/>
          <stop offset="0.5" stop-color="var(--bean-mid)"/>
          <stop offset="1" stop-color="var(--bean-dark)"/>
        </linearGradient>
      </defs>
      <path d="M0,14 C30,4 55,20 85,12 C115,4 140,18 170,10 C200,3 230,16 260,9 C280,5 292,10 300,8 L300,90 L0,90 Z" fill="url(#beans)"/>
      <path d="M0,14 C30,4 55,20 85,12 C115,4 140,18 170,10 C200,3 230,16 260,9 C280,5 292,10 300,8" fill="none" stroke="var(--label-cream)" stroke-width="2"/>
    </svg>
  </div>
</body>
</html>
```